Easy Marinade Labels for Butchery Store

Need a set of labels designed for a Butchery Shop. They will sit in the top left corner of the packets as a triangle (7cm each side). Easy because the only major requirement is the label name and some small text saying "Please ask in store to see spec sheet for ingredients". Extra points for finding a fun way to incorporate the logo and/or images of food (garlic bulbs, chilli, spices ect) to enhance the label. List of Marinade Names below: GarlicPepper Mint & RosemarySatayBBQChilli Plum & GingerSundried Tomato & BasilBuffaloHoney SoyHoi-SinPer PeriSpicy CajunTeriyakiBlack Bean Ive also attached the logo and an example of how the label might sit on a packet of meat. Thanks

Target Market(s)

Butchery Deli Shop Customers

Industry/Entity Type

Food Store

Font styles to use
Serif
Sans Serif
Decorative
Other font styles liked:
• Fun font that isn't a generic Quillbrenn Font?

Colors

Designer to choose colors to be used in the design.

Requirements
Must have
• Product Name
• Small text saying "Please ask in store to see spec sheet for ingredients"
Nice to have
• Photos of ingredients that would match that type of marinade - Chilli, Garlic, Spices.
• Tavo Crest Logo - not essential if it doesn't look good on the label / doesn't fit.

```html
<!DOCTYPE html>
<html lang="en">
<head>
<meta charset="utf-8">
<title>Tavo Crest Marinade Labels</title>
<link rel="stylesheet" href="https://fonts.googleapis.com/css2?family=Montserrat:wght@600;800&display=swap">
<style>
  :root {
    --canvas: #3a3a3a;
    --label-white: #f3f3f3;
    --label-green: #2f6e1d;
    --label-dark: #262626;
    --band-red: #b00f14;
    --band-text: #ffffff;
    --band-note: #f6d9d9;
    --brand-red: #a3161a;
    --brand-light: #f1e6d8;
  }
  * { margin: 0; padding: 0; box-sizing: border-box; }
  html, body {
    width: 994px;
    height: 1200px;
    overflow: hidden;
    background: var(--canvas);
  }
  .sheet {
    position: relative;
    width: 994px;
    height: 1200px;
    font-family: "Montserrat", sans-serif;
  }
  .label { position: absolute; display: block; filter: drop-shadow(0 6px 8px rgba(0,0,0,0.45)); }
  .label--hero { left: 267px; top: 90px; width: 460px; height: 460px; }
  .label--small { top: 800px; width: 300px; height: 300px; }
  .label--white-small { left: 40px; }
  .label--green { left: 347px; }
  .label--dark { left: 654px; }
  .label__base--white { fill: var(--label-white); }
  .label__base--green { fill: var(--label-green); }
  .label__base--dark { fill: var(--label-dark); }
  .label__band { fill: var(--band-red); }
  .label__name {
    fill: var(--band-text);
    font-family: "Montserrat", sans-serif;
    font-weight: 800;
    font-size: 21px;
    letter-spacing: 0.4px;
  }
  .label__note {
    fill: var(--band-note);
    font-family: "Montserrat", sans-serif;
    font-weight: 600;
    font-size: 6.6px;
    letter-spacing: 0.2px;
  }
  .brand__name {
    font-family: "Montserrat", sans-serif;
    font-weight: 800;
    font-size: 16px;
  }
  .brand__name--on-light { fill: var(--brand-red); }
  .brand__name--on-color { fill: var(--brand-light); }
</style>
</head>
<body>
<main class="sheet">

  <svg class="label label--hero" viewBox="0 0 320 320" aria-label="Garlic and Peppermint marinade label, white">
    <defs>
      <radialGradient id="herb-art" cx="50%" cy="55%" r="55%">
        <stop offset="0%" stop-color="#e9ddd2"/>
        <stop offset="60%" stop-color="#8cc26a"/>
        <stop offset="100%" stop-color="#5fae3a" stop-opacity="0"/>
      </radialGradient>
    </defs>
    <path class="label__base--white" d="M0,18 Q0,0 18,0 L320,0 L0,320 Z"/>
    <polygon class="label__band" points="258,0 320,0 0,320 0,258"/>
    <ellipse role="img" aria-label="Illustration of a garlic bulb with fresh mint leaves" cx="76" cy="60" rx="44" ry="40" fill="url(#herb-art)"/>
    <text class="brand__name brand__name--on-light" x="22" y="122">Tavo Crest</text>
    <text class="label__name" x="141" y="141" text-anchor="middle" dominant-baseline="middle" transform="rotate(-45 141 141)">GARLIC AND PEPPERMINT</text>
    <text class="label__note" x="151" y="151" text-anchor="middle" dominant-baseline="middle" transform="rotate(-45 151 151)">Please ask in store to see spec sheet for ingredients</text>
  </svg>

  <svg class="label label--small label--white-small" viewBox="0 0 320 320" aria-label="Garlic and Peppermint marinade label, white">
    <path class="label__base--white" d="M0,18 Q0,0 18,0 L320,0 L0,320 Z"/>
    <polygon class="label__band" points="258,0 320,0 0,320 0,258"/>
    <ellipse role="img" aria-label="Illustration of a garlic bulb with fresh mint leaves" cx="76" cy="60" rx="44" ry="40" fill="url(#herb-art)"/>
    <text class="brand__name brand__name--on-light" x="22" y="122">Tavo Crest</text>
    <text class="label__name" x="141" y="141" text-anchor="middle" dominant-baseline="middle" transform="rotate(-45 141 141)">GARLIC AND PEPPERMINT</text>
    <text class="label__note" x="151" y="151" text-anchor="middle" dominant-baseline="middle" transform="rotate(-45 151 151)">Please ask in store to see spec sheet for ingredients</text>
  </svg>

  <svg class="label label--small label--green" viewBox="0 0 320 320" aria-label="Garlic and Peppermint marinade label, green">
    <path class="label__base--green" d="M0,18 Q0,0 18,0 L320,0 L0,320 Z"/>
    <polygon class="label__band" points="258,0 320,0 0,320 0,258"/>
    <ellipse role="img" aria-label="Illustration of a garlic bulb with fresh mint leaves" cx="76" cy="60" rx="44" ry="40" fill="url(#herb-art)"/>
    <text class="brand__name brand__name--on-color" x="22" y="122">Tavo Crest</text>
    <text class="label__name" x="141" y="141" text-anchor="middle" dominant-baseline="middle" transform="rotate(-45 141 141)">GARLIC AND PEPPERMINT</text>
    <text class="label__note" x="151" y="151" text-anchor="middle" dominant-baseline="middle" transform="rotate(-45 151 151)">Please ask in store to see spec sheet for ingredients</text>
  </svg>

  <svg class="label label--small label--dark" viewBox="0 0 320 320" aria-label="Garlic and Peppermint marinade label, black">
    <path class="label__base--dark" d="M0,18 Q0,0 18,0 L320,0 L0,320 Z"/>
    <polygon class="label__band" points="258,0 320,0 0,320 0,258"/>
    <ellipse role="img" aria-label="Illustration of a garlic bulb with fresh mint leaves" cx="76" cy="60" rx="44" ry="40" fill="url(#herb-art)"/>
    <text class="brand__name brand__name--on-color" x="22" y="122">Tavo Crest</text>
    <text class="label__name" x="141" y="141" text-anchor="middle" dominant-baseline="middle" transform="rotate(-45 141 141)">GARLIC AND PEPPERMINT</text>
    <text class="label__note" x="151" y="151" text-anchor="middle" dominant-baseline="middle" transform="rotate(-45 151 151)">Please ask in store to see spec sheet for ingredients</text>
  </svg>

</main>
</body>
</html>
```